Business Card Design

Hoping for a black background business card, minimalistic design.
With the Marble Crest logo you created in white.

I would like to include:
My Name and title
Address (street address)
Reception: (phone number)
Fax: (fax number)
Reception: (email address)
Direct email: (email address)
Instagram: (ig handle)

```html
<!DOCTYPE html>
<html lang="en">
<head>
<meta charset="UTF-8">
<title>Marble Crest – Business Card</title>
<link href="https://fonts.googleapis.com/css2?family=Montserrat:wght@500&family=Open+Sans:wght@400;700&display=swap" rel="stylesheet">
<style>
  :root {
    --stage: #3b3b3b;
    --card: #111111;
    --ink: #ffffff;
    --ink-soft: #bdbdbd;
    --ink-muted: #8a8a8a;
    --rule: #777777;
    --ring: #2a2a2a;
  }
  * { margin: 0; padding: 0; box-sizing: border-box; }
  html, body { width: 1200px; height: 801px; overflow: hidden; }
  body {
    background: var(--stage);
    display: flex;
    align-items: center;
    justify-content: center;
    gap: 40px;
    font-family: "Open Sans", Arial, sans-serif;
    color: var(--ink);
  }
  .card {
    width: 525px;
    height: 300px;
    background: var(--card);
    position: relative;
    box-shadow: 0 12px 30px rgba(0,0,0,.35);
  }

  /* Front: contact side */
  .card--contact { display: flex; align-items: center; }
  .brand-lockup {
    width: 250px;
    display: flex;
    align-items: center;
    justify-content: center;
    gap: 12px;
  }
  .brand-dot {
    width: 30px; height: 30px;
    border: 2px solid var(--ink);
    border-radius: 50%;
    flex: none;
  }
  .wordmark {
    font-family: "Montserrat", Arial, sans-serif;
    font-weight: 500;
    letter-spacing: 3px;
    text-transform: uppercase;
    color: var(--ink);
  }
  .brand-lockup .wordmark { font-size: 17px; }
  .divider {
    width: 1px;
    height: 210px;
    background: var(--rule);
  }
  .details { padding-left: 22px; font-size: 13px; line-height: 1.5; }
  .person-name { font-weight: 700; font-size: 16px; letter-spacing: .5px; text-transform: uppercase; }
  .person-title { color: var(--ink-soft); margin-bottom: 12px; }
  .address { margin-bottom: 12px; }
  .contact-list { list-style: none; }
  .contact-list li { display: flex; align-items: center; gap: 7px; }
  .contact-list svg { width: 11px; height: 11px; fill: var(--ink); flex: none; }
  .note { color: var(--ink-muted); font-size: 11px; }

  /* Back: brand side */
  .brand-ring {
    position: absolute;
    left: 30px; top: 24px;
    width: 250px; height: 250px;
    border-radius: 50%;
    border: 14px solid var(--ring);
    box-shadow: inset 0 2px 3px rgba(255,255,255,.08), 0 2px 3px rgba(255,255,255,.05);
  }
  .card--brand .wordmark {
    position: absolute;
    right: 28px; bottom: 52px;
    font-size: 22px;
  }
</style>
</head>
<body>
  <section class="card card--contact">
    <div class="brand-lockup">
      <span class="brand-dot"></span>
      <span class="wordmark">Marble Crest</span>
    </div>
    <div class="divider"></div>
    <div class="details">
      <p class="person-name">Daniel Hart</p>
      <p class="person-title">President</p>
      <p class="address">2480 Alder Lane, Suite 210<br>Fairview, OR 97024</p>
      <ul class="contact-list">
        <li><svg viewBox="0 0 16 16"><path d="M3 1l3 3-1.5 2a9 9 0 0 0 5.5 5.5L12 10l3 3-2 2C6 15 1 10 1 3z"/></svg>503.555.0142 <span class="note">(Reception)</span></li>
        <li><svg viewBox="0 0 16 16"><path d="M4 1h8v4H4zM1 6h14v7h-3v2H4v-2H1zM5 10v4h6v-4z"/></svg>503.555.0142 <span class="note">(Fax)</span></li>
        <li><svg viewBox="0 0 16 16"><path d="M1 3h14v10H1zM2 4l6 5 6-5"/></svg>info@marblecrest.com <span class="note">(Reception)</span></li>
        <li><svg viewBox="0 0 16 16"><path d="M1 3h14v10H1zM2 4l6 5 6-5"/></svg>Daniel@marblecrest.com <span class="note">(Direct)</span></li>
        <li><svg viewBox="0 0 16 16"><circle cx="8" cy="8" r="7"/></svg>www.marblecrest.com</li>
      </ul>
    </div>
  </section>

  <section class="card card--brand">
    <div class="brand-ring"></div>
    <span class="wordmark">Marble Crest</span>
  </section>
</body>
</html>
```